Birch Spire Kilo Marsh website

we need a website to cater to 2 aspect of the business. We have Birch spire residence and birch spire office. For the office, we will get their inquire and arrange a face to face meetup to show them the office area for rent. For the residence side, it will need to be like stayrio or velupa.com. we want to allow them to book online for the date they need. We have a total of 10 different room configurations starting at $70 per night and up depending on the size of the room. example of the design is https://lumbrahaven.com/

Target Market(s)

the website should have detail information on the layout, designs, and luxury of the building.

Industry/Entity Type

office and service appartment rental/lease

Coding

Coded - Design and coding required

Number of Pages Required

5+ page

Requirements
Must have
• a luxury perspective
Nice to have
• example https://lumbrahaven.com/

```html
<!DOCTYPE html>
<html lang="en">
<head>
<meta charset="utf-8">
<title>Birch Spire Kilo Marsh</title>
<link rel="stylesheet" href="https://fonts.googleapis.com/css2?family=Cinzel:wght@400;500;600&family=Lato:wght@400;700&display=swap">
<style>
:root{
  --gold:#c9972f;
  --ink:#141414;
  --text:#333;
  --muted:#777;
  --board:#999999;
  --soft:#f4f4f4;
  --white:#fff;
  --black:#000;
}
*{margin:0;padding:0;box-sizing:border-box}
html,body{width:679px;height:1200px;overflow:hidden;background:var(--board)}
.board{position:absolute;left:0;top:0;width:1456px;height:2575px;transform:scale(0.46634);transform-origin:0 0;background:var(--board);font-family:'Lato',sans-serif;color:var(--text)}
.abs{position:absolute}
.serif{font-family:'Cinzel',serif}
.gold{color:var(--gold)}
.photo{position:absolute}
.page{position:absolute;left:30px;top:33px;width:680px;height:2505px;background:var(--white);overflow:hidden}
.hero{position:absolute;left:0;top:0;width:680px;height:340px;background:linear-gradient(160deg,#3a3d40 0%,#26282b 55%,#1a1c1e 100%)}
.brand{position:absolute;text-align:center;font-family:'Cinzel',serif}
.brand-mark{display:block;margin:0 auto 6px;border:2px solid currentColor;border-radius:50%}
.menu span{display:block;height:2px;background:var(--white);margin-bottom:5px;margin-left:auto}
.btn{position:absolute;display:flex;align-items:center;justify-content:center;font-family:'Cinzel',serif;font-weight:600;font-size:10px;letter-spacing:.4px;background:var(--gold);color:var(--ink)}
.btn-light{background:var(--white);color:var(--ink);font-size:12px}
.btn-outline{background:transparent;border:1.5px solid var(--gold);color:var(--gold)}
.h-sec{position:absolute;left:0;width:680px;text-align:center;font-family:'Cinzel',serif;font-size:21px;color:var(--ink);letter-spacing:.3px}
.p-center{position:absolute;left:100px;width:480px;text-align:center;font-size:8.5px;line-height:17.5px;color:var(--text)}
.feature h3{position:absolute;font-family:'Cinzel',serif;font-size:17px;font-weight:500;color:var(--ink);white-space:nowrap}
.feature p{position:absolute;width:200px;font-size:8.5px;line-height:16.5px;color:var(--text)}
.card{position:absolute;top:1704px;width:170px;height:110px;background:var(--white);box-shadow:0 2px 10px rgba(0,0,0,.09);border-radius:3px;text-align:center}
.avatar{position:absolute;left:65px;top:-22px;width:40px;height:40px;border-radius:50%;background:linear-gradient(#c9c9c9,#8a8a8a);border:2px solid #eee}
.card h4{margin-top:27px;font-size:10px;font-weight:700;color:var(--ink)}
.stars{font-size:7px;color:var(--gold);letter-spacing:1px;margin-top:2px}
.card p{font-size:7.5px;line-height:14.5px;color:var(--muted);padding:2px 10px 0}
.card.mid p{color:var(--text)}
.contact{position:absolute;left:0;top:1920px;width:680px;height:358px;background:var(--soft)}
.field{position:absolute;background:var(--white);border:1px solid #e0c78f;font-size:8.5px;font-weight:700;color:var(--ink);padding-left:14px;display:flex;align-items:center}
.field.area{align-items:flex-start;padding-top:14px}
.footer{position:absolute;left:0;top:2278px;width:680px;height:227px;background:var(--black);color:var(--white)}
.col{position:absolute;top:43px}
.col h5{font-family:'Cinzel',serif;font-size:11px;font-weight:500;letter-spacing:.4px;margin-bottom:9px}
.col li{list-style:none;font-size:8.5px;height:19.5px;display:flex;align-items:center}
.col li svg{margin-right:5px}
.ci{display:flex;align-items:flex-start;font-size:8.5px;line-height:15px;margin-bottom:9px}
.ci .ico{flex:none;width:18px;height:18px;border-radius:50%;background:var(--white);display:flex;align-items:center;justify-content:center;margin-right:8px}
.social{position:absolute;top:2444px;width:18px;height:18px;border-radius:50%;background:var(--white)}
.landing{position:absolute;left:742px;top:33px;width:679px;height:388px;background:var(--white);overflow:hidden}
</style>
</head>
<body>
<div class="board">

  <main class="page">
    <section class="hero" role="img" aria-label="Dim open-plan office interior with desks and plants">
      <div class="brand" style="left:63px;top:14px;width:93px;color:var(--white);font-size:11px">
        <span class="brand-mark" style="width:26px;height:26px"></span>Birch Spire Kilo Marsh
      </div>
      <div class="menu abs" style="left:595px;top:32px;width:22px">
        <span style="width:16px"></span><span style="width:22px"></span><span style="width:14px"></span>
      </div>
      <h1 class="h-sec" style="top:124px;color:var(--white);font-size:22px;font-weight:500">Welcome to Birch Spire Office</h1>
      <div class="btn btn-light" style="left:288px;top:171px;width:103px;height:31px">GET STARTED</div>
    </section>

    <h2 class="h-sec" style="top:364px">About <span class="gold">Birch Spire Kilo Marsh</span></h2>
    <p class="p-center" style="top:396px">Nam libero tempore, cum soluta nobis est eligendi optio cumque nihil impedit quo minus id quod maxime placeat facere possimus, omnis voluptas assumenda est, omnis dolor repellendus. Temporibus autem quibusdam et aut officiis debitis aut rerum necessitatibus saepe eveniet ut et voluptates repudiandae sint et molestiae non recusandae.</p>
    <p class="p-center" style="top:466px">Itaque earum rerum hic tenetur a sapiente delectus, ut aut reiciendis voluptatibus maiores alias consequatur aut perferendis doloribus asperiores repellat.</p>
    <div class="btn" style="left:291px;top:518px;width:96px;height:31px">READ MORE</div>

    <section class="feature">
      <div class="photo" style="left:311px;top:591px;width:369px;height:301px;background:linear-gradient(135deg,#e9e9e9,#b8b8b8 60%,#8e8e8e)" role="img" aria-label="Bright office with glass partitions and long desks"></div>
      <h3 style="left:62px;top:658px">Temporibus <span class="gold">Autem</span></h3>
      <p style="left:63px;top:688px">Nam libero tempore, cum soluta nobis est eligendi nda est, poribus autem quibusdam et aut officiis t et epudiandae sint et molestiae non recusandae.</p>
      <p style="left:63px;top:754px">Itaque earum rerum hic tenetur a sapiente delectus, ut aut reiciendis voluptatibus maiores alias consequatur aut perferendis doloribus asperiores repellat.</p>
    </section>

    <section class="feature">
      <div class="photo" style="left:0;top:944px;width:366px;height:300px;background:linear-gradient(120deg,#d9d6cf,#9a6a48 50%,#5b4030)" role="img" aria-label="Office with brick wall, wooden ceiling and workstations"></div>
      <h3 style="left:418px;top:1010px">Emporibus <span class="gold">Autem</span></h3>
      <p style="left:418px;top:1040px">Nam libero tempore, cum soluta nobis est eligendi nda est, poribus autem quibusdam et aut officiis t et epudiandae sint et molestiae non recusandae.</p>
      <p style="left:418px;top:1106px">Itaque earum rerum hic tenetur a sapiente delectus, ut aut reiciendis voluptatibus maiores alias consequatur aut perferendis doloribus asperiores repellat.</p>
    </section>

    <section class="feature">
      <div class="photo" style="left:311px;top:1302px;width:369px;height:301px;background:linear-gradient(135deg,#f1f1f1,#c9d3da 55%,#9aa6ad)" role="img" aria-label="Large white office hall with columns and windows"></div>
      <h3 style="left:62px;top:1368px">Mporibus <span class="gold">Autem</span></h3>
      <p style="left:63px;top:1399px">Nam libero tempore, cum soluta nobis est eligendi nda est, poribus autem quibusdam et aut officiis t et epudiandae sint et molestiae non recusandae.</p>
      <p style="left:63px;top:1465px">Itaque earum rerum hic tenetur a sapiente delectus, ut aut reiciendis voluptatibus maiores alias consequatur aut perferendis doloribus asperiores repellat.</p>
    </section>

    <h2 class="h-sec" style="top:1638px">What <span class="gold">Customer Says</span></h2>
    <div class="card" style="left:63px"><div class="avatar" role="img" aria-label="Customer portrait"></div><h4>Marcus Feld</h4><div class="stars">★★★★★</div><p>Temporibus autem quibusdam et aut officiis debitis aut rerum necessitatibus saepe eveniet ut et voluptates</p></div>
    <div class="card mid" style="left:255px"><div class="avatar" role="img" aria-label="Customer portrait"></div><h4>Owen Brask</h4><div class="stars">★★★★★</div><p>Itaque earum rerum hic tenetur a sapiente delectus, reiciendis voluptatibus maiores alias consequatur aut</p></div>
    <div class="card" style="left:447px"><div class="avatar" role="img" aria-label="Customer portrait"></div><h4>Clara Venn</h4><div class="stars">★★★★★</div><p>Nam libero tempore, cum soluta nobis est eligendi optio cumque nihil impedit quo minus id quod</p></div>
    <div class="btn" style="left:291px;top:1848px;width:96px;height:31px">VIEW MORE</div>

    <section class="contact">
      <h2 class="h-sec" style="top:30px">Contact <span class="gold">Us</span></h2>
      <div class="field" style="left:63px;top:72px;width:266px;height:33px">Name</div>
      <div class="field" style="left:350px;top:72px;width:265px;height:33px">Email</div>
      <div class="field" style="left:63px;top:121px;width:266px;height:38px">Phone Number</div>
      <div class="field" style="left:350px;top:121px;width:265px;height:38px">Address</div>
      <div class="field area" style="left:63px;top:169px;width:553px;height:91px">Message</div>
      <div class="btn" style="left:291px;top:284px;width:96px;height:32px">SUBMIT</div>
    </section>

    <footer class="footer">
      <div class="brand" style="left:60px;top:44px;width:148px;color:var(--gold);font-size:15px">
        <span class="brand-mark" style="width:40px;height:40px;margin-bottom:12px"></span>Birch Spire Kilo Marsh
      </div>
      <div class="col" style="left:244px"><h5>Quick Links</h5><ul>
        <li><svg width="8" height="8" viewBox="0 0 8 8"><path d="M0 4h6M4 1l3 3-3 3" stroke="#fff" stroke-width="1.4" fill="none"/></svg>Home</li>
        <li><svg width="8" height="8" viewBox="0 0 8 8"><path d="M0 4h6M4 1l3 3-3 3" stroke="#fff" stroke-width="1.4" fill="none"/></svg>About</li>
        <li><svg width="8" height="8" viewBox="0 0 8 8"><path d="M0 4h6M4 1l3 3-3 3" stroke="#fff" stroke-width="1.4" fill="none"/></svg>Services</li>
        <li><svg width="8" height="8" viewBox="0 0 8 8"><path d="M0 4h6M4 1l3 3-3 3" stroke="#fff" stroke-width="1.4" fill="none"/></svg>Testimonials</li>
        <li><svg width="8" height="8" viewBox="0 0 8 8"><path d="M0 4h6M4 1l3 3-3 3" stroke="#fff" stroke-width="1.4" fill="none"/></svg>Contact Us</li>
      </ul></div>
      <div class="col" style="left:375px"><h5>Help Links</h5><ul>
        <li><svg width="8" height="8" viewBox="0 0 8 8"><path d="M0 4h6M4 1l3 3-3 3" stroke="#fff" stroke-width="1.4" fill="none"/></svg>FAQ</li>
        <li><svg width="8" height="8" viewBox="0 0 8 8"><path d="M0 4h6M4 1l3 3-3 3" stroke="#fff" stroke-width="1.4" fill="none"/></svg>Terms of use</li>
        <li><svg width="8" height="8" viewBox="0 0 8 8"><path d="M0 4h6M4 1l3 3-3 3" stroke="#fff" stroke-width="1.4" fill="none"/></svg>Privacy Policy</li>
        <li><svg width="8" height="8" viewBox="0 0 8 8"><path d="M0 4h6M4 1l3 3-3 3" stroke="#fff" stroke-width="1.4" fill="none"/></svg>Support Links</li>
        <li><svg width="8" height="8" viewBox="0 0 8 8"><path d="M0 4h6M4 1l3 3-3 3" stroke="#fff" stroke-width="1.4" fill="none"/></svg>Conditions</li>
      </ul></div>
      <div class="col" style="left:498px"><h5>Contact Us</h5>
        <div class="ci"><span class="ico"><svg width="9" height="11" viewBox="0 0 9 11"><path d="M4.5 0A4 4 0 0 0 .5 4c0 3 4 7 4 7s4-4 4-7a4 4 0 0 0-4-4z" fill="#000"/><circle cx="4.5" cy="4" r="1.5" fill="#fff"/></svg></span><span>Birch Spire Kilo Marsh<br>United States</span></div>
        <div class="ci"><span class="ico"><svg width="10" height="10" viewBox="0 0 10 10"><path d="M2 0.5l2 2.2-1 1.2a6 6 0 0 0 3 3l1.2-1 2.2 2-1.4 1.6C4.5 9.5 0.5 5.5 0.4 1.9z" fill="#000"/></svg></span><span>+1 555 010 2040</span></div>
        <div class="ci"><span class="ico"><svg width="10" height="8" viewBox="0 0 10 8"><rect width="10" height="8" rx="1" fill="#000"/><path d="M0.5 1l4.5 3.5L9.5 1" stroke="#fff" fill="none"/></svg></span><span>info@birchspirekm.com</span></div>
      </div>
      <div class="abs" style="left:63px;top:216px;width:553px;height:1px;background:#555"></div>
      <div class="abs" style="left:0;top:237px;width:680px;text-align:center;font-size:8.5px;font-weight:700">Copyrights@2024.Birch Spire Kilo Marsh.All Rights Reserved</div>
    </footer>
  </main>
  <span class="social" style="left:93px"></span>
  <span class="social" style="left:125px"></span>
  <span class="social" style="left:158px"></span>
  <span class="social" style="left:191px"></span>

  <section class="landing">
    <div class="abs" style="left:488px;top:0;width:191px;height:388px;background:linear-gradient(160deg,#c99530,#b8862a 60%,#d09f36)"></div>
    <div class="photo" style="left:356px;top:62px;width:262px;height:262px;border-radius:50%;border:3px solid var(--white);background:radial-gradient(circle at 45% 40%,#f2f2f2,#bdbdbd 60%,#6e6e6e)" role="img" aria-label="Modern white office reception with plants"></div>
    <div class="brand" style="left:56px;top:14px;width:106px;color:var(--gold);font-size:11px">
      <span class="brand-mark" style="width:28px;height:28px"></span>Birch Spire Kilo Marsh
    </div>
    <div class="abs serif" style="left:63px;top:111px;font-size:11px;font-weight:500;color:var(--ink)">WELCOME TO</div>
    <h2 class="abs serif" style="left:63px;top:133px;font-size:20px;font-weight:500;color:var(--ink);white-space:nowrap">BIRCH SPIRE KILO MARSH</h2>
    <p class="abs" style="left:65px;top:169px;width:215px;font-size:8.5px;line-height:15.5px">Itaque earum rerum hic tenetur a sapiente delectus, ut aut reiciendis voluptatibus maiores alias consequatur aut perferendis doloribus asperiores repellat.</p>
    <div class="btn" style="left:64px;top:232px;width:107px;height:27px;font-size:8.5px">BIRCH SPIRE OFFICE</div>
    <div class="btn btn-outline" style="left:201px;top:232px;width:121px;height:27px;font-size:8px">BIRCH SPIRE RESIDENCE</div>
  </section>

</div>
</body>
</html>
```